Postcard Design

We are an upscale, full service real estate boutique based in Mt. Pleasant, SC. We will be having a Grand Opening of our beautiful, new office complete with high end custom home architecture and design. I will attach photos for your review. I would like to come up with a medium postcard to be mailed to clientele of Mt. Pleasant. Home prices between $300,000 - $2.2 million. The customers can call our office for the Grand Opening Listing Promotion or stop by our grand opening. We will have drawings for door prizes that include services at Brambleton Day Spa, Copper Kettle gift certificates, and they can register to win a cruise with a listing presentation. Our Grand Opening will be a couple of different dates, April 7, 2016 and April 21, 2016. I will want an order that lists the 7th and another order that will list the 21. The look should have a very "relaxing, beach" feel, but not Myrtle Beach...should reflect colors of the ocean, like you are on vacation. I will include logos and pics for your review. Thank you!

```html
<!DOCTYPE html>
<html lang="en">
<head>
<meta charset="utf-8">
<title>Saltmarsh Real Estate – Grand Opening Postcard</title>
<link rel="stylesheet" href="https://fonts.googleapis.com/css2?family=PT+Sans+Narrow:wght@400;700&family=Oswald:wght@500&family=Open+Sans:wght@400&display=swap">
<style>
  :root {
    --backdrop: #ece9e4;
    --ocean-top: #5ec3cf;
    --ocean-mid: #9fd9d6;
    --foam: #eef3f0;
    --sand: #e6dccd;
    --brand-blue: #2a9fd0;
    --link-blue: #1f8ccf;
    --coral-red: #e43a2c;
    --ink: #1e1e1e;
    --muted: #7b7b7b;
    --blush: #d9cbc6;
    --bloom-yellow: #f6e58f;
    --bloom-coral: #ef8a6e;
    --leaf-green: #2f8a5a;
  }
  * { margin: 0; padding: 0; box-sizing: border-box; }
  html, body { width: 1200px; height: 500px; overflow: hidden; background: var(--backdrop); }
  body { position: relative; font-family: "PT Sans Narrow", "Arial Narrow", sans-serif; color: var(--ink); }

  .card { position: absolute; top: 37px; height: 431px; overflow: hidden; box-shadow: 0 2px 6px rgba(0,0,0,0.18); }
  .card--front { left: 25px; width: 560px;
    background: linear-gradient(172deg, var(--ocean-top) 0%, var(--ocean-mid) 38%, var(--foam) 62%, var(--sand) 80%, #ddd1bf 100%); }
  .card--back { left: 608px; width: 562px; background: linear-gradient(90deg, var(--blush) 0%, #efe8e5 35%, #ffffff 62%); }

  .abs { position: absolute; }
  .center { text-align: center; }

  .front-panel { left: 0; top: 0; }
  .bloom { position: absolute; }

  .brand { color: var(--brand-blue); font-weight: 700; letter-spacing: 2px; }
  .brand-mark { display: block; margin: 0 auto 4px; width: 34px; height: 34px; border-radius: 50%; border: 3px solid var(--brand-blue); }
  .brand-name { font-size: 24px; line-height: 1; }
  .brand-sub { font-size: 10px; letter-spacing: 3px; color: var(--brand-blue); font-weight: 700; }

  .front-brand { left: 60px; width: 250px; top: 28px; }
  .headline { left: 20px; width: 320px; top: 108px; font-family: "Oswald", sans-serif; font-size: 26px; color: var(--coral-red); letter-spacing: 1px; }
  .date { left: 20px; width: 320px; top: 148px; font-family: "Open Sans", sans-serif; font-size: 19px; color: var(--brand-blue); }
  .address { left: 20px; width: 320px; top: 176px; font-size: 15px; line-height: 18px; }
  .divider { left: 130px; top: 216px; }
  .invite { left: 20px; width: 320px; top: 231px; font-size: 13.5px; line-height: 16.5px; font-weight: 700; color: var(--link-blue); }
  .phone { font-family: "Open Sans", sans-serif; font-size: 16px; display: inline-flex; align-items: center; gap: 5px; }
  .front-phone { left: 20px; width: 320px; top: 286px; justify-content: center; display: flex; color: var(--coral-red); }
  .prizes { left: 90px; width: 160px; top: 312px; font-size: 13.5px; line-height: 16.5px; white-space: nowrap; display: flex; flex-direction: column; align-items: center; }
  .prizes strong { color: var(--link-blue); }

  .house-photo { left: 340px; top: 120px; width: 184px; height: 135px; border: 4px solid #fff; border-radius: 12px;
    background: linear-gradient(180deg, #a9c7e2 0%, #cfd9e2 40%, #8fa3a6 65%, #6f8b4e 100%); }
  .tagline { left: 379px; top: 276px; font-size: 15px; line-height: 18px; color: var(--link-blue); }
  .web { font-size: 11.5px; letter-spacing: 1px; color: var(--muted); }
  .front-web { left: 358px; top: 384px; }

  .top-band { left: 130px; right: 0; top: 0; height: 15px; background: linear-gradient(90deg, rgba(42,159,208,0) 0%, #9dc6e6 40%, #2f7fc4 100%); }
  .back-brand { left: 360px; width: 140px; top: 32px; }
  .back-brand .brand-name { font-size: 20px; }
  .stamp { left: 484px; top: 36px; width: 56px; height: 56px; border: 3px dashed #b5b5b5; }
  .mail-address { left: 367px; top: 104px; font-size: 14px; line-height: 17px; }
  .about-title { left: 35px; top: 68px; font-size: 17px; font-weight: 400; color: var(--link-blue); }
  .about-text { left: 35px; top: 90px; width: 250px; font-size: 13px; line-height: 15.2px; }
  .back-call { left: 60px; width: 200px; top: 290px; font-size: 13px; line-height: 16px; }
  .back-phone { left: 60px; width: 200px; top: 340px; display: flex; justify-content: center; color: var(--link-blue); }
  .back-web { left: 82px; top: 366px; }
</style>
</head>
<body>

<section class="card card--front">
  <svg class="abs front-panel" width="340" height="431" viewBox="0 0 340 431" aria-hidden="true">
    <path d="M0 0 H300 C250 120 350 260 290 431 H0 Z" fill="rgba(255,255,255,0.72)"/>
  </svg>

  <div class="bloom" role="img" aria-label="Tropical flowers and leaves" style="right:0;top:0;width:130px;height:90px;background:radial-gradient(circle at 70% 30%, var(--bloom-coral) 0 18%, var(--bloom-yellow) 19% 42%, rgba(246,229,143,0) 70%);"></div>
  <div class="bloom" role="img" aria-label="Tropical flowers and leaves" style="left:0;bottom:0;width:82px;height:170px;background:radial-gradient(ellipse at 30% 75%, var(--bloom-yellow) 0 20%, var(--bloom-coral) 21% 34%, var(--leaf-green) 35% 50%, rgba(47,138,90,0) 70%);"></div>

  <div class="abs front-brand center">
    <span class="brand-mark"></span>
    <div class="brand brand-name">SALTMARSH</div>
    <div class="brand-sub">REAL ESTATE</div>
  </div>

  <h1 class="abs headline center">GRAND OPENING</h1>
  <p class="abs date center">Thursday | April 7, 2016</p>
  <p class="abs address center">1250 Harbor Road<br>North Mount Pleasant, SC 29466</p>

  <svg class="abs divider" width="100" height="10" viewBox="0 0 100 10" aria-hidden="true">
    <line x1="0" y1="5" x2="42" y2="5" stroke="#4fb9c8" stroke-width="1.5"/>
    <circle cx="50" cy="5" r="4" fill="#4fb9c8"/>
    <line x1="58" y1="5" x2="100" y2="5" stroke="#4fb9c8" stroke-width="1.5"/>
  </svg>

  <p class="abs invite center">You are invited to call our office for the<br>Grand Opening Listing Promotion or<br>stop by our grand opening.</p>

  <p class="abs front-phone phone">
    <svg width="14" height="14" viewBox="0 0 14 14" aria-hidden="true"><circle cx="7" cy="7" r="6.2" fill="none" stroke="currentColor" stroke-width="1.3"/><path d="M4.5 4 Q4 8 9.5 10 L10 8.6 L8.6 7.8 L7.8 8.5 Q6 7.6 5.7 5.8 L6.4 5.1 L5.7 3.8 Z" fill="currentColor"/></svg>
    843.555.0142
  </p>

  <p class="abs prizes">
    <span>We will have drawings for door prizes that</span>
    <span>include services at <strong>Brambleton Day Spa,</strong></span>
    <span><strong>Copper Kettle gift certificates</strong>,</span>
    <span>and you can register to win a <strong>cruise</strong></span>
    <span>with a listing presentation.</span>
  </p>

  <div class="abs house-photo" role="img" aria-label="Photograph of the new two-storey office building among trees"></div>
  <p class="abs tagline">Experience<br>the difference . . .</p>
  <p class="abs web front-web">www.saltmarshrealestate.com</p>
</section>

<section class="card card--back">
  <div class="abs top-band"></div>
  <div class="bloom" role="img" aria-label="Tropical flowers and leaves" style="left:0;top:0;width:120px;height:60px;background:radial-gradient(ellipse at 30% 25%, var(--bloom-coral) 0 16%, var(--leaf-green) 17% 40%, rgba(47,138,90,0) 70%);"></div>
  <div class="bloom" role="img" aria-label="Yellow hibiscus flowers" style="left:234px;top:322px;width:48px;height:48px;background:radial-gradient(circle, var(--bloom-yellow) 0 40%, rgba(246,229,143,0) 70%);"></div>

  <div class="abs back-brand center">
    <span class="brand-mark"></span>
    <div class="brand brand-name">SALTMARSH</div>
    <div class="brand-sub">REAL ESTATE</div>
  </div>
  <div class="abs stamp"></div>
  <p class="abs mail-address">1250 Harbor Road<br>North Mount Pleasant<br>South Carolina 29466</p>

  <h2 class="abs about-title">ABOUT SALTMARSH REAL ESTATE</h2>
  <p class="abs about-text">Saltmarsh Real Estate is a full service real estate company that specializes in high-end customer service from the moment we answer your call or email. When you step into the Saltmarsh way, get ready to experience the difference as we rally our team around you! Gone are the days of having to pull your team of people together (mortgage, insurance, inspectors, contractors, etc.) to get to the closing table! When you become a client of Saltmarsh, we will do all of the work for you, just sit back and relax and let us do what we do best, sell real estate . . . while keeping you informed each and every step of the way!</p>

  <p class="abs back-call center">Call us for the<br>Grand Opening Listing Promotion or<br>stop by our grand opening.</p>
  <p class="abs back-phone phone">
    <svg width="14" height="14" viewBox="0 0 14 14" aria-hidden="true"><circle cx="7" cy="7" r="6.2" fill="none" stroke="currentColor" stroke-width="1.3"/><path d="M4.5 4 Q4 8 9.5 10 L10 8.6 L8.6 7.8 L7.8 8.5 Q6 7.6 5.7 5.8 L6.4 5.1 L5.7 3.8 Z" fill="currentColor"/></svg>
    843.555.0142
  </p>
  <p class="abs web back-web">www.saltmarshrealestate.com</p>
</section>

</body>
</html>
```